Business Card for Beach theme sports bar called TAVRU

I need a business card designed for our employees, front and back. This will be used by the employees of two business locations to hand out to customers. I've attached the previous business cards we used at one time for a Benwicks (it is now Tavru). Looking for a fresh new card that is elegant but has character.

Target Market(s)

30-60, middle class

Contact Information for Business Card

We are a beach bar and sports bar. I am looking for an elegant business card with the front to have the TAVRU logo. Then on the back I need it to allow a space for employees to write their names and for them to write in their schedule. I have attached our old cards with our old name Benwicks so you can pull everything we need on the cards. one thing is missing is we have another location at 2815 N Willow Crest Rd with a number of 702-418-9351. Since we will use it for both locations it should allow the employee to circle or check mark the bar which they work at.

Font styles to use
Sans Serif

Requirements
Must have
• We are looking for some fresh ideas for the business card. Something that will really stick out to customers when the staff hands them out. Creativity will be looked at positively, but we still want it to look upscale and fun.

```html
<!DOCTYPE html>
<html lang="en">
<head>
<meta charset="utf-8">
<title>Tavru – Business Card, Front and Back</title>
<link rel="stylesheet" href="https://fonts.googleapis.com/css2?family=Josefin+Sans:wght@300;400;600&display=swap">
<style>
  :root {
    --page: #ffffff;
    --card: #cdbc93;
    --card-shade: rgba(0,0,0,0.22);
    --ink: #5b3f2c;
    --ink-soft: #6a5140;
    --accent: #c8262e;
    --ghost: #e2d4ac;
    --sans: "Josefin Sans", sans-serif;
  }
  * { box-sizing: border-box; margin: 0; padding: 0; }
  html, body { width: 1200px; height: 583px; overflow: hidden; background: var(--page); }
  .canvas { position: relative; width: 1200px; height: 583px; font-family: var(--sans); color: var(--ink); }

  .card {
    position: absolute;
    background: var(--card);
    box-shadow: 0 2px 10px var(--card-shade);
    overflow: hidden;
  }

  /* Front */
  .card--front { left: 21px; top: 41px; width: 367px; height: 210px; }
  .brand {
    position: absolute; left: 0; right: 0; top: 82px;
    display: flex; align-items: center; justify-content: center; gap: 10px;
  }
  .brand__dot { width: 14px; height: 14px; border-radius: 50%; background: var(--accent); }
  .brand__name { font-size: 44px; font-weight: 600; color: var(--ink); line-height: 1; letter-spacing: 1px; }

  /* Back */
  .card--back { left: 24px; top: 346px; width: 363px; height: 205px; }
  .back__ghost-name {
    position: absolute; left: 6px; top: 30px;
    font-size: 112px; font-weight: 600; color: var(--ghost); line-height: 1;
    letter-spacing: 2px;
  }
  .back__name-line {
    position: absolute; left: 16px; top: 108px; width: 284px; height: 1px; background: var(--ink-soft);
  }
  .location {
    position: absolute; top: 114px; width: 150px; margin-left: -75px;
    text-align: center; font-size: 11px; font-weight: 300; line-height: 15px; color: var(--ink);
  }
  .location--first { left: 86px; }
  .location--second { left: 243px; }
  .location__check {
    display: block; width: 13px; height: 13px; margin: 0 auto 8px;
    border: 1.5px solid var(--ink-soft);
  }
  .location__phone { margin-top: 3px; }
  .back__email {
    position: absolute; left: 0; width: 344px; top: 186px; text-align: center;
    font-size: 14px; font-weight: 300; letter-spacing: 2px; color: var(--ink);
  }
  .schedule {
    position: absolute; left: 320px; top: 16px; width: 22px;
    list-style: none; border: 1.5px solid var(--ink-soft);
  }
  .schedule__day {
    height: 24px; display: flex; align-items: center; justify-content: center;
    font-size: 14px; font-weight: 300; color: var(--ink);
    border-bottom: 1.5px solid var(--ink-soft);
  }
  .schedule__day:last-child { border-bottom: none; }
</style>
</head>
<body>
<main class="canvas">

  <section class="card card--front" aria-label="Card front">
    <div class="brand">
      <span class="brand__dot"></span>
      <span class="brand__name">Tavru</span>
    </div>
  </section>

  <section class="card card--back" aria-label="Card back">
    <div class="back__ghost-name" aria-hidden="true">Tavru</div>
    <div class="back__name-line" aria-label="Space for employee name"></div>

    <div class="location location--first">
      <span class="location__check"></span>
      <p>3140 W Cedar Bluff Rd</p>
      <p>Las Vegas, NV 89 146</p>
      <p class="location__phone">702 593 6124</p>
    </div>

    <div class="location location--second">
      <span class="location__check"></span>
      <p>2815 N Willow Crest Rd</p>
      <p>Las Vegas, NV 89 146</p>
      <p class="location__phone">702-418-9351</p>
    </div>

    <p class="back__email">cs@tavrubar.com</p>

    <ul class="schedule" aria-label="Work schedule">
      <li class="schedule__day">M</li>
      <li class="schedule__day">T</li>
      <li class="schedule__day">W</li>
      <li class="schedule__day">Th</li>
      <li class="schedule__day">F</li>
      <li class="schedule__day">Sa</li>
      <li class="schedule__day">Su</li>
    </ul>
  </section>

</main>
</body>
</html>
```